Feature film needs look book digital brochure - Media/Investor's package

Looking for a designer to create an edgy, eye popping visual representation of my film to get interest from investors, producers and actors, along with Investor and Sponsorship information. Basically it would introduce the project and in about 9-13 pages; give an overview of the film, why to invest, an artistic statement and potential casting ideas and an introduction to the key crew. I have included images (probably more than you need), our film's key art (iron dusk final image & bib logo), and our company (Morvane)'s logo. I've also included samples for another film (gtkr_proposal.pdf) and a proposal I already did for the film. The sample for the other film is more visual and something I'd like to emulate.

The film is called Iron Dusk: a sports drama about two triathletes who overcome their personal demons to train for and compete in the biggest race of their lives.

```html
<!DOCTYPE html>
<html lang="en">
<head>
<meta charset="utf-8">
<title>Iron Dusk – Synopsis</title>
<link href="https://fonts.googleapis.com/css2?family=Tinos:wght@400;700&display=swap" rel="stylesheet">
<style>
  :root {
    --ink: #ffffff;
    --foliage-dark: #1f2a18;
    --foliage: #4a5a2c;
    --sunlight: #c9a45a;
    --asphalt: #4a4c50;
    --asphalt-dark: #2a2b2e;
    --road-line: #d9a11e;
    --panel: rgba(10, 10, 12, 0.5);
  }
  * { margin: 0; padding: 0; box-sizing: border-box; }
  html, body { width: 885px; height: 1200px; overflow: hidden; }
  body { font-family: "Tinos", "Times New Roman", serif; color: var(--ink); }

  .page {
    position: relative;
    width: 885px;
    height: 1200px;
    overflow: hidden;
    background: var(--asphalt-dark);
  }
  .backdrop { position: absolute; inset: 0; width: 885px; height: 1200px; }
  .frame {
    position: absolute;
    left: 14px; top: 14px; right: 14px; bottom: 18px;
    border: 2px solid var(--ink);
  }
  .title {
    position: absolute;
    left: 124px; top: 72px;
    font-weight: 700;
    font-size: 74px;
    letter-spacing: 5px;
    line-height: 1;
  }
  .story {
    position: absolute;
    left: 86px; top: 166px;
    width: 756px;
    font-size: 14.4px;
    line-height: 17.4px;
    text-align: center;
  }
  .story-slant {
    float: left;
    width: 440px;
    height: 900px;
    shape-outside: polygon(0 0, 1% 0, 100% 100%, 0 100%);
  }
  .story p { margin-bottom: 17px; }
  .story .opening { text-indent: 0; }
  .credit {
    position: absolute;
    right: 46px; top: 1068px;
    font-size: 14.4px;
  }
</style>
</head>
<body>
<main class="page">
  <svg class="backdrop" viewBox="0 0 885 1200" role="img" aria-label="Photograph of a wet mountain road through sunlit forest with a swimmer breaking the water surface in the lower left">
    <defs>
      <linearGradient id="scene" x1="0" y1="0" x2="0.6" y2="1">
        <stop offset="0" stop-color="var(--foliage-dark)"/>
        <stop offset="0.2" stop-color="var(--foliage)"/>
        <stop offset="0.38" stop-color="#6c6a4a"/>
        <stop offset="0.6" stop-color="var(--asphalt)"/>
        <stop offset="1" stop-color="var(--asphalt-dark)"/>
      </linearGradient>
      <radialGradient id="glow" cx="0.68" cy="0.05" r="0.35">
        <stop offset="0" stop-color="var(--sunlight)" stop-opacity="0.75"/>
        <stop offset="1" stop-color="var(--sunlight)" stop-opacity="0"/>
      </radialGradient>
    </defs>
    <rect width="885" height="1200" fill="url(#scene)"/>
    <rect width="885" height="1200" fill="url(#glow)"/>
    <path d="M520 1200 L885 880 L885 920 L580 1200 Z" fill="var(--road-line)" opacity="0.55"/>
    <polygon points="150,168 842,168 842,1060 540,1060" fill="var(--panel)"/>
  </svg>

  <div class="frame"></div>

  <h1 class="title">SYNOPSIS...</h1>

  <section class="story">
    <div class="story-slant"></div>
    <p class="opening">Thousands of swimmers pile over one another, cyclists speed down a hill at 80kph, and runners summon every ounce of their soul to make it to the finish line. This is their story… This is the story of Iron Dusk.</p>
    <p>TREVOR is in the twilight of his semi-professional triathlete career. His girlfriend, CORA, has always been supportive and until recently, used to go to all the events with him and cheer him on. To Trevor, their relationship has become more of a burden and a distraction. After coming second in a big race in Austria, Trevor lashes out at Cora and she dumps him, the culmination of years of emotional abuse. Depressed, rejected, and alone, Cora decides a change is needed. With Cora no longer providing extra financial support, Trevor reluctantly accepts a young rival’s request for coaching.</p>
    <p>After facing serious anxiety over a life seemingly wasted, Cora goes on a long evening run, longer than she’s ever taken before. She returns home, sweaty and sore, but inspired. She goes on another run, and another and becomes fiercely determined to train every day, dragging LEXI, her best friend, with her to the beach to watch her swim. Lexi thinks Cora is doing this to get back into a relationship with Trevor and does not hide her disapproval. Lexi and Cora have a major falling out and Cora is left to face the challenge of a triathlon without the support of her best friend. Driven by a newly discovered competitive spirit and a new community she’s found through running, Cora races a local triathlon and qualifies for the World Championships, the same race her ex-boyfriend is fighting to win. Her training intensifies as she battles her conflicted soul.</p>
    <p>Trevor’s become a little distracted by VANESSA, a reporter doing an exposé on him and his year of redemption. During a race, Trevor hits a set back and is unable to continue the race. He explodes with blame, anger, and fury on the course. Meanwhile his biggest competitor, SEBASTIAN KUREK, has just won another major competition. As Trevor opens up to Vanessa like he’s never done before to anyone, she ends the relationship; she’s just not the right girl for him.</p>
    <p>Trevor the veteran and Cora the new kid on the block – both facing the World Championships alone. Following an interview with the press, Trevor runs into Cora causing all her insecurities and doubts to resurface again. Trevor’s guilt over how he treated her impacts his once-unwavering desire to win. During the race, Cora, never having competed in anything so grueling as this, fights off every urge to quit, her instinctual response to adversity in the past. Trevor is faced with another challenge of his own. When an unforeseen accident occurs on the course, Trevor has to decide whether he will explode in blame and anger or to finish what he started.</p>
    <p>They meet at the 13 Mile Aid Station, the halfway mark of the “run” segment of the triathlon. Exhausted and fatigued, they run the last iron dusk together. They cross the line one minute before the finish cut off. The greatest race of their life, completed - not because of a finishing time or a medal, but the personal journey each has traversed to get to this moment, together.</p>
  </section>

  <p class="credit">Iron Dusk Proposal – Halden Ware Grant – J</p>
</main>
</body>
</html>
```